professional looking data specialist website

I've recently had a new logo designed and I'm now looking to get a professional looking website built. This is for a new company that specialises in data. We look to support companies with business intelligence, report modelling, data governance to new european legislation (GDPR). We are offer consultancy or we can attend site and complete work when required. Our target arket is united kingdom wide and we are specifically aiming at small to medium sized companies.

Target Market(s)

small to medium enterprise companies from all industries

Industry/Entity Type

Professional Service

Coding

Coded - Design and coding required

Number of Pages Required

4 page

Font styles to use
Sans Serif

Colors

Designer to choose colors to be used in the design.

Requirements
Must have
• Professional look including the company logo, need to have ability to request more information from us so needs a inquiries page, seperate pages for the different offerings, data governance, report modelling, business intelligence implementation, data protection
Nice to have
• any website interaction, animation, etc
Should not have
• too many colours, too busy pages, must look professional

```html
<!DOCTYPE html>
<html lang="en">
<head>
<meta charset="utf-8">
<title>Dataline Ltd</title>
<link href="https://fonts.googleapis.com/css2?family=Raleway:wght@400;500;600;700&display=swap" rel="stylesheet">
<style>
:root{
  --blue:#1b6fc2;
  --blue-light:#3d8fdf;
  --ink:#333;
  --grey:#888;
  --footer:#2b2b2b;
  --footer-line:#3a3a3a;
  --white:#fff;
}
*{box-sizing:border-box;margin:0;padding:0}
html,body{width:776px;height:1200px;overflow:hidden}
body{position:relative;background:var(--white);font-family:'Raleway',sans-serif;color:var(--ink)}
.abs{position:absolute}
.topline{left:0;top:0;width:776px;height:2px;background:var(--blue)}
.header{left:0;top:2px;width:776px;height:86px;border-bottom:1px solid #e3e3e3}
.brand{left:52px;top:30px;display:flex;align-items:center;gap:8px}
.brand-mark{width:22px;height:22px;background:var(--blue)}
.brand-name{font-size:22px;font-weight:600;color:var(--blue)}
.top-contact{top:14px;display:flex;align-items:center;gap:5px;font-size:12px;font-weight:600;color:#555}
.top-contact .ico{width:19px;height:19px;border:1px solid #999;border-radius:3px;display:flex;align-items:center;justify-content:center}
.top-contact.mail{font-size:8.5px;font-weight:500}
.nav{top:62px;font-size:11px;color:#444}
.nav.active{color:var(--blue)}
.nav-mark{left:429px;top:45px;width:11px;height:11px;background:var(--blue)}
.nav-sep{top:64px;width:1px;height:10px;background:#ddd}
.hero{left:0;top:88px;width:776px;height:325px;overflow:hidden;
  background:
    radial-gradient(ellipse 170px 110px at 400px 170px,rgba(70,150,215,.85),rgba(120,180,225,.45) 55%,transparent 100%),
    radial-gradient(ellipse 150px 150px at 660px 120px,rgba(232,188,160,.9),rgba(225,190,170,.35) 60%,transparent 100%),
    radial-gradient(ellipse 130px 120px at 330px 250px,rgba(230,186,158,.8),transparent 100%),
    radial-gradient(ellipse 140px 90px at 230px 80px,rgba(255,255,255,.95),transparent 100%),
    linear-gradient(100deg,#eef1f3 0%,#e3e9ed 35%,#cbd9e3 65%,#aebfcb 100%)}
.hero-deco{left:62px;top:70px}
.hero-caption{left:0;top:278px;width:776px;height:47px;background:rgba(55,62,70,.85);color:var(--white);font-weight:700;font-size:15.5px;text-align:center;line-height:19px;padding-top:4px;text-shadow:0 1px 2px rgba(0,0,0,.5)}
.arrow{top:131px;width:24px;height:22px;background:#3a3a3a;display:flex;align-items:center;justify-content:center}
.section-title{left:0;width:776px;text-align:center;font-size:21px;font-weight:500;color:#666}
.section-title b{color:var(--blue);font-weight:600}
.rule{left:362px;width:52px;height:1px;background:#bbb}
.card{top:507px;width:158px;height:138px;border:3px solid #cfcfcf;border-radius:4px;padding:5px}
.card.active{border-color:var(--blue)}
.card-img{width:100%;height:100%}
.card-label{top:652px;width:158px;text-align:center;font-size:13.5px;font-weight:500;line-height:16px;color:var(--ink)}
.card-label.active{color:var(--blue)}
.welcome-text{left:56px;top:801px;width:664px;text-align:center;font-family:Arial,sans-serif;font-size:9.6px;line-height:14.8px;color:#333}
.btn{left:347px;top:874px;width:82px;height:23px;background:var(--blue);color:var(--white);font-size:10.5px;display:flex;align-items:center;padding-left:7px;gap:7px}
.btn span.sq{width:12px;height:12px;border:1.5px solid #cfe0f3}
.footer{left:0;top:930px;width:776px;height:241px;background:var(--footer)}
.f-title{color:var(--white);font-size:13px;font-weight:500}
.field{left:53px;width:196px;border:1px solid #8a8a8a;color:var(--white);font-size:8.5px;font-weight:500;padding:3px 8px}
.send{left:53px;top:1125px;width:64px;height:20px;background:var(--blue);color:var(--white);font-size:10px;font-weight:600;display:flex;align-items:center;justify-content:center}
.f-divider{top:980px;width:1px;height:150px;background:var(--footer-line)}
.qlink{left:308px;font-size:10.5px;color:var(--white);display:flex;align-items:center;gap:6px}
.qlink::before{content:"";width:4px;height:4px;background:var(--blue)}
.qlink.active{color:var(--blue-light)}
.follow{left:309px;top:1091px;color:var(--white);font-size:10px;font-weight:600}
.social{top:1085px;width:20px;height:20px;border:1px solid #aaa;border-radius:2px;display:flex;align-items:center;justify-content:center}
.social span{width:8px;height:8px;border-radius:50%;background:#d6d6d6}
.c-item{left:565px;display:flex;align-items:flex-start;gap:8px;color:var(--white);font-size:9.5px;line-height:12px}
.c-item svg{flex:none}
.copyright{left:0;top:1171px;width:776px;height:29px;background:var(--blue);color:var(--white);font-size:10px;display:flex;align-items:center;justify-content:center}
</style>
</head>
<body>
<div class="abs topline"></div>
<header class="abs header"></header>
<div class="abs brand"><span class="brand-mark"></span><span class="brand-name">Dataline Ltd</span></div>

<div class="abs top-contact" style="left:498px">
  <span class="ico"><svg width="11" height="11" viewBox="0 0 24 24"><path fill="#1b6fc2" d="M6.6 10.8a15 15 0 006.6 6.6l2.2-2.2c.3-.3.7-.4 1-.2 1.1.4 2.3.6 3.6.6.6 0 1 .4 1 1V20c0 .6-.4 1-1 1A17 17 0 013 4c0-.6.4-1 1-1h3.5c.6 0 1 .4 1 1 0 1.3.2 2.5.6 3.6.1.3 0 .7-.2 1z"/></svg></span>
  (020)-555-0148
</div>
<div class="abs top-contact mail" style="left:619px">
  <span class="ico"><svg width="11" height="9" viewBox="0 0 22 16"><rect width="22" height="16" rx="2" fill="#1b6fc2"/><path d="M1 1l10 8 10-8" stroke="#fff" stroke-width="2" fill="none"/></svg></span>
  info@dataline-ltd.com
</div>

<div class="abs nav-mark"></div>
<div class="abs nav active" style="left:420px">Home</div>
<div class="abs nav-sep" style="left:472px"></div>
<div class="abs nav" style="left:493px">About Us</div>
<div class="abs nav-sep" style="left:561px"></div>
<div class="abs nav" style="left:582px">Services</div>
<div class="abs nav-sep" style="left:646px"></div>
<div class="abs nav" style="left:668px">Contact Us</div>

<section class="abs hero" role="img" aria-label="Hands using a tablet showing business charts beside a coffee cup">
  <div class="abs arrow" style="left:4px"><svg width="8" height="10" viewBox="0 0 8 10"><path d="M6 1L2 5l4 4" stroke="#fff" stroke-width="2" fill="none"/></svg></div>
  <div class="abs arrow" style="left:748px"><svg width="8" height="10" viewBox="0 0 8 10"><path d="M2 1l4 4-4 4" stroke="#fff" stroke-width="2" fill="none"/></svg></div>
  <div class="abs hero-caption">Offering Consultancy Services From Small To Medium EnterprisesCompanies To All<br>Industries In The UK</div>
</section>

<h2 class="abs section-title" style="top:440px">Our <b>Services</b></h2>
<div class="abs rule" style="top:477px"></div>

<div class="abs card active" style="left:72px"><div class="card-img" role="img" aria-label="Hand holding glowing data charts" style="background:linear-gradient(160deg,#1b1f4a,#3a3aa0 55%,#7a5cd0)"></div></div>
<div class="abs card" style="left:243px"><div class="card-img" role="img" aria-label="Tablet with bar and pie charts on a desk" style="background:linear-gradient(150deg,#bfe6f8,#5fc0ec 55%,#e9f6fc)"></div></div>
<div class="abs card" style="left:414px"><div class="card-img" role="img" aria-label="Person working at a computer showing reports" style="background:linear-gradient(150deg,#e6e9ec,#c8d0d7 50%,#f3f3f3)"></div></div>
<div class="abs card" style="left:586px"><div class="card-img" role="img" aria-label="Padlock on a circuit board" style="background:radial-gradient(circle at 50% 55%,#6fb4e6,#1b3f73 55%,#0d1d38)"></div></div>

<div class="abs card-label active" style="left:72px">Data<br>Governance</div>
<div class="abs card-label" style="left:243px">Business Intelligence<br>Implementation</div>
<div class="abs card-label" style="left:414px">Report<br>Modeling</div>
<div class="abs card-label" style="left:586px">Data<br>Protection</div>

<h2 class="abs section-title" style="top:750px;font-weight:600;color:#777">Welcome To <b>Dataline Ltd</b></h2>
<div class="abs rule" style="top:787px"></div>
<p class="abs welcome-text">Lorem ipsum dolor sit amet, consectetuer adipiscing elit, sed diam nonummy nibh euismod tincidunt ut laoreet dolore magna aliquam erat volutpat. Ut wisi enim ad minim veniam, quis nostrud exerci tation ullamcorper suscipit lobortis nisl ut aliquip ex ea commodo consequat. Duis autem vel eum iriure dolor in hendrerit in vulputate velit esse molestie consequat, vel illum dolore eu feugiat nulla facilisis at vero eros et accumsan et iusto odio dignissim qui blandit praesent luptatum zzril delenit augue duis dolore te feugait nulla facilisi.</p>
<div class="abs btn">Read More <span class="sq"></span></div>

<footer class="abs footer"></footer>
<div class="abs f-title" style="left:55px;top:967px">Quick Inquiry</div>
<div class="abs field" style="top:1002px;height:19px">Name</div>
<div class="abs field" style="top:1024px;height:19px">Email</div>
<div class="abs field" style="top:1045px;height:19px">Subject</div>
<div class="abs field" style="top:1066px;height:53px">Message</div>
<div class="abs send">SEND</div>

<div class="abs f-divider" style="left:276px"></div>
<div class="abs f-title" style="left:308px;top:967px">Quick Links</div>
<div class="abs qlink active" style="top:1003px">Home</div>
<div class="abs qlink" style="top:1021px">About Us</div>
<div class="abs qlink" style="top:1039px">Services</div>
<div class="abs qlink" style="top:1057px">Contact Us</div>
<div class="abs follow">Follow Us</div>
<div class="abs social" style="left:358px" aria-label="Social profile"><span></span></div>
<div class="abs social" style="left:384px" aria-label="Social profile"><span></span></div>
<div class="abs social" style="left:408px" aria-label="Social profile"><span></span></div>
<div class="abs social" style="left:433px" aria-label="Social profile"><span></span></div>

<div class="abs f-divider" style="left:530px"></div>
<div class="abs f-title" style="left:572px;top:976px">Contact Details</div>
<div class="abs c-item" style="top:1002px">
  <svg width="11" height="15" viewBox="0 0 12 16"><path fill="#1b6fc2" d="M6 0a6 6 0 016 6c0 4-6 10-6 10S0 10 0 6a6 6 0 016-6z"/><circle cx="6" cy="6" r="2.2" fill="#2b2b2b"/></svg>
  <span>Loren ipsum dolor sit amet mbert<br>Roundabout, London SE9 4QX.</span>
</div>
<div class="abs c-item" style="top:1038px">
  <svg width="11" height="12" viewBox="0 0 24 24"><path fill="#1b6fc2" d="M6.6 10.8a15 15 0 006.6 6.6l2.2-2.2c.3-.3.7-.4 1-.2 1.1.4 2.3.6 3.6.6.6 0 1 .4 1 1V20c0 .6-.4 1-1 1A17 17 0 013 4c0-.6.4-1 1-1h3.5c.6 0 1 .4 1 1 0 1.3.2 2.5.6 3.6.1.3 0 .7-.2 1z"/></svg>
  <span>020-555-0148</span>
</div>
<div class="abs c-item" style="top:1064px">
  <svg width="11" height="11" viewBox="0 0 12 12"><rect x="2" y="0" width="8" height="4" fill="#1b6fc2"/><rect x="0" y="4" width="12" height="6" rx="1" fill="#1b6fc2"/><rect x="3" y="8" width="6" height="4" fill="#1b6fc2"/></svg>
  <span>020-555-0148</span>
</div>
<div class="abs c-item" style="top:1091px">
  <svg width="11" height="9" viewBox="0 0 22 16"><rect width="22" height="16" rx="2" fill="#1b6fc2"/><path d="M1 1l10 8 10-8" stroke="#2b2b2b" stroke-width="2" fill="none"/></svg>
  <span>hello@dataline-ltd.com</span>
</div>

<div class="abs copyright">Copyright © 2017 Dataline Ltd . All Right Reserved</div>
</body>
</html>
```